Album Artwork needed for House of Worship

We are a church called Lanternfield Church in New Jersey. We are a new church and just passed our two year mark.

This is our first album and it is entitled "Open Wide Skies" with a smaller text saying "Congregational Songs from Lanternfield Church".

Our album is based off of songs sung in our weekly services. It has a mix of contemporary christian, traditional and original songs.

We love creativity. Some of the album art we like are Brookvane, Marrow, Tinfolk, Rhea Vollmer's new album "Quiet Rising Tide"and Ember Harvest.

We are open to creativity outside of these examples.

In total we would need about 4 pages of designs for this project. One is the cover. The second is behind the cover. The third is the back of the album. The last is on the CD itself.

We have attached a word document with the specifics for what is to be on each page. We have also attached songs for you to listen and know our sound.

Thank you!

Target Market(s)

Church, Christians, Young Adults, Adults, College students

Industry/Entity Type

Church

Font styles to use
Decorative

Requirements
Must have
• Title: "Open Wide Skies" followed by "Congregational Songs from Lanternfield Church"
Nice to have
• We uploaded a shade of blue we would like to see on the album.
• Our church logo on the back of the album

```html
<!DOCTYPE html>
<html lang="en">
<head>
<meta charset="utf-8">
<title>Open Wide Skies — Album Cover</title>
<link rel="stylesheet" href="https://fonts.googleapis.com/css2?family=Big+Shoulders+Display:wght@300&family=Oswald:wght@400&display=swap">
<style>
  :root {
    --sky-teal: #3f8f8e;
    --sky-violet: #3b3f8c;
    --sky-deep: #26307a;
    --haze-rose: #8a8585;
    --field-dark: #1f4a4c;
    --field-mid: #2f6564;
    --glow-red: rgba(232, 52, 79, 0.85);
    --glow-coral: rgba(226, 120, 90, 0.75);
    --glow-gold: rgba(217, 199, 100, 0.7);
    --glow-ice: rgba(150, 205, 212, 0.75);
    --ink-white: #ffffff;
  }
  * { margin: 0; padding: 0; box-sizing: border-box; }
  html, body { width: 1200px; height: 1200px; overflow: hidden; background: #111; }
  .album-cover { position: relative; width: 1200px; height: 1200px; overflow: hidden; }
  .landscape-backdrop {
    position: absolute; inset: 0;
    background:
      radial-gradient(ellipse 60% 45% at 95% 5%, var(--sky-deep) 0%, transparent 70%),
      radial-gradient(ellipse 70% 40% at 10% 8%, var(--sky-teal) 0%, transparent 75%),
      linear-gradient(180deg, transparent 0%, transparent 45%, var(--haze-rose) 55%, var(--field-mid) 68%, var(--field-dark) 100%),
      linear-gradient(100deg, var(--sky-teal) 0%, #4a7e8c 45%, var(--sky-violet) 100%);
  }
  .artwork-glow {
    position: absolute;
    left: 228px; top: 25px; width: 720px; height: 755px;
    background:
      radial-gradient(ellipse 45% 50% at 35% 40%, var(--glow-red) 0%, transparent 100%),
      radial-gradient(ellipse 40% 45% at 72% 35%, var(--glow-coral) 0%, transparent 100%),
      radial-gradient(ellipse 30% 35% at 88% 20%, var(--glow-gold) 0%, transparent 100%);
  }
  .artwork-accent {
    position: absolute;
    left: 552px; top: 815px; width: 155px; height: 240px;
    background: radial-gradient(ellipse 50% 50% at 50% 55%, var(--glow-ice) 0%, transparent 100%);
  }
  .cover-type { position: absolute; inset: 0; width: 1200px; height: 1200px; }
  .album-title {
    font-family: "Big Shoulders Display", "Antonio", sans-serif;
    font-weight: 300; font-size: 94px; fill: var(--ink-white);
  }
  .album-subtitle {
    font-family: "Oswald", sans-serif;
    font-weight: 400; font-size: 38px; fill: var(--ink-white);
  }
</style>
</head>
<body>
  <main class="album-cover">
    <div class="landscape-backdrop" role="img" aria-label="Photograph of a dusky mountain ridge above a grassy field under a teal and violet sky"></div>
    <div class="artwork-glow" role="img" aria-label="Large translucent geometric illustration in red, coral and gold tones"></div>
    <div class="artwork-accent" role="img" aria-label="Small pale blue geometric illustration floating above the field"></div>
    <svg class="cover-type" viewBox="0 0 1200 1200" xmlns="http://www.w3.org/2000/svg">
      <text class="album-title" x="133" y="450" textLength="967" lengthAdjust="spacing">OPEN WIDE SKIES</text>
      <text class="album-subtitle" x="303" y="638" textLength="622" lengthAdjust="spacingAndGlyphs">CONGREGATIONAL SONGS FROM LANTERNFIELD CHURCH</text>
    </svg>
  </main>
</body>
</html>
```